pelikorax.gr wordpress makeover

We need a makeover of our wordpress website pelikorax.gr We are a company that provides astrology services via phone either by billable phone number or by prepaid packages.This is what we sell. Moreover, we share everyday astrology related articles to our blog. It will be a multy page website. Our goal is always to sell our phone prepaid packages or to make the visitor of the website call our billable numbers. Our website should have:
-a home page introducing its content (astrologers, call packages, blog section with categories).
-astrologers page (you can see the existing one to understand)
-Phone packages page (eshop page where you can buy prepaid phone packages. woo commerce maybe)
- Blog page divined by categories.
The website should have places for display banners eg. a sidebar.
I will provide some screen shots of websites we like. You can always visit our existing website www.pelikorax.gr to see it for yourself.

Target Market(s)

people seeking for future telling - astrologer services via phone. People who like to be informed about everyday astrology predictions

Industry/Entity Type

Astrology - tarot services via phone

Coding

Coded - Design and coding required

Number of Pages Required

5+ page

Font styles to use
Decorative
Script

Colors
6B429C
8869AF
B7A5CE
E3DAEB
F3F0F8

Requirements
Must have
• -Home page -Astrologers page -Phone packages page (eshop) -Blog page with categories - Made following the guidelines of google so as to be efficient in google ads marketing. Mobile friendly.
Nice to have
• Nice call to action buttons to call or buy packages. Sidebar with banner ads of maybe our offers.

```html
<!DOCTYPE html>
<html lang="en">
<head>
<meta charset="utf-8">
<title>pelikorax.gr – Home</title>
<link href="https://fonts.googleapis.com/css2?family=Poppins:wght@400;500;600;700;800&display=swap" rel="stylesheet">
<style>
:root{
  --purple:#6B429C;
  --purple-mid:#8869AF;
  --purple-soft:#B7A5CE;
  --purple-pale:#E3DAEB;
  --purple-light:#F3F0F8;
  --ink:#1c1830;
  --muted:#6a6478;
  --white:#fff;
  --footer:#232127;
}
*{box-sizing:border-box;margin:0;padding:0}
html,body{width:1200px;height:2704px;overflow:hidden}
body{font-family:"Poppins",sans-serif;color:var(--ink);background:var(--white);position:relative}
a{color:inherit;text-decoration:none}

.topbar{height:52px;display:flex;align-items:center;justify-content:space-between;padding:0 12px 0 18px}
.brand{font-size:26px;font-weight:500;color:var(--ink)}
.hotline{height:42px;width:300px;background:linear-gradient(90deg,#fff 0%,var(--purple-light) 40%);display:flex;align-items:center;justify-content:flex-end;gap:8px;padding-right:8px;border-radius:4px}
.hotline small{font-size:10px;line-height:1.1;color:var(--purple);text-align:right;font-weight:500}
.hotline strong{font-size:30px;font-weight:800;color:var(--purple);letter-spacing:-1px}

.mainnav{height:32px;background:var(--purple);display:flex;align-items:center;padding:0 18px;gap:28px}
.mainnav a{color:var(--white);font-size:11px;font-weight:600;letter-spacing:.3px}
.mainnav .nav-cta{margin-left:auto;background:var(--white);color:var(--purple);padding:5px 16px;border-radius:3px;font-size:10px}

.hero{position:relative;height:616px;background:radial-gradient(circle at 68% 45%,#3c4fa0 0%,#262a66 35%,#15163a 75%);overflow:hidden}
.hero-art{position:absolute;left:560px;top:10px;width:600px;height:600px;border-radius:50%;background:radial-gradient(circle,#5a73c8 0%,#33408e 55%,transparent 72%);opacity:.75}
.hero-copy{position:absolute;left:72px;top:150px;width:620px;color:var(--white)}
.hero-copy h1{font-size:48px;line-height:1.12;font-weight:700;text-transform:uppercase}
.hero-copy p{margin-top:16px;max-width:470px;font-size:16px;line-height:1.6;font-weight:500}
.btn{display:inline-block;font-weight:600;border-radius:3px}
.btn-read{margin-top:26px;background:var(--purple);color:var(--white);padding:13px 22px;font-size:13px;text-transform:uppercase}
.hero-dots{position:absolute;left:72px;bottom:16px;display:flex;gap:10px}
.hero-dots span{width:9px;height:9px;border-radius:50%;background:rgba(255,255,255,.45)}
.hero-dots span:first-child{background:var(--white)}

.featured{position:relative;height:1212px;background:linear-gradient(180deg,var(--purple-pale),var(--purple-light) 60%,var(--purple-pale))}
.section-title{position:absolute;left:72px;top:104px;font-size:32px;font-weight:800;text-transform:uppercase;color:var(--ink)}
.section-title::after{content:"";display:block;width:300px;height:3px;background:var(--purple);margin-top:8px}
.article-grid{position:absolute;left:72px;top:180px;width:700px;display:grid;grid-template-columns:328px 332px;column-gap:40px;row-gap:20px}
.article-card{height:312px}
.article-thumb{height:188px;border-radius:2px}
.t1{background:linear-gradient(135deg,#c8a07a,#6a7fa8)}
.t2{background:linear-gradient(135deg,#e6d2b8,#4b7c9e)}
.t3{background:linear-gradient(135deg,#6fb2d6,#d7a455)}
.t4{background:linear-gradient(135deg,#2a1c1a,#a04a2c)}
.t5{background:linear-gradient(135deg,#f1a23c,#6c3a8a)}
.t6{background:linear-gradient(135deg,#5a3a2a,#d98a4a)}
.article-card h3{margin-top:16px;font-size:26px;line-height:1.15;font-weight:700}
.article-meta{margin-top:10px;font-size:12px;color:var(--muted);display:flex;align-items:center;gap:8px}
.article-meta i{display:inline-block;width:10px;height:10px;background:var(--purple);border-radius:2px}
.article-meta b{color:var(--purple);font-weight:600}

.sidebar{position:absolute;left:796px;top:104px;width:332px}
.astro-box{background:var(--white);border-radius:4px;padding:18px 24px 28px;height:736px}
.astro-box h2{font-size:28px;font-weight:800;text-transform:uppercase}
.astro-item{margin-top:28px}
.astro-head{display:flex;gap:14px}
.astro-photo{width:80px;height:80px;border-radius:4px;background:linear-gradient(135deg,var(--purple-soft),var(--purple-mid))}
.astro-head h4{font-size:16px;color:var(--purple);font-weight:600}
.astro-head p{font-size:13px;line-height:1.4;color:var(--muted)}
.btn-call{margin-top:14px;display:flex;align-items:center;gap:14px;width:250px;height:44px;background:var(--purple);color:var(--white);border-radius:22px;font-size:19px;font-weight:700;padding-left:4px}
.btn-call .icon{width:36px;height:36px;border-radius:50%;background:var(--white);display:flex;align-items:center;justify-content:center}
.btn-more{display:block;margin:30px auto 0;width:168px;border:1px solid var(--purple);color:var(--ink);text-align:center;padding:10px 0;font-size:15px;font-weight:500;border-radius:3px}
.ad-banner{margin-top:40px;height:290px;border-radius:4px;background:radial-gradient(circle at 45% 40%,#2f5bd2,#0d1858 70%);position:relative;color:var(--white)}
.ad-banner .ad-time{position:absolute;right:28px;top:24px;font-size:42px;font-weight:800}
.ad-banner .ad-price{position:absolute;right:24px;bottom:22px;font-size:48px;font-weight:800}

.packages{position:relative;height:596px;background:linear-gradient(120deg,#3a1e66,var(--purple) 50%,#8b4fb5)}
.packages h2{position:absolute;width:100%;top:60px;text-align:center;color:var(--white);font-size:34px;font-weight:700;text-transform:uppercase}
.package-row{position:absolute;left:72px;top:160px;display:flex;gap:28px}
.package-card{width:246px;height:360px;background:var(--white);border-radius:8px;overflow:hidden;text-align:center}
.package-top{height:160px;background:linear-gradient(160deg,#2b2560,#171637);color:var(--white);padding-top:24px}
.package-top h5{font-size:18px;font-weight:600}
.package-top .price{font-size:44px;font-weight:800;line-height:1.15}
.package-top .mins{font-size:16px;font-weight:600}
.package-card p{padding:22px 24px 0;font-size:13px;line-height:1.5;color:var(--muted)}
.btn-info{margin-top:22px;background:var(--purple);color:var(--white);font-size:13px;padding:10px 34px}
.arrow{position:absolute;top:340px}
.arrow.left{left:20px}.arrow.right{right:20px}

.site-footer{position:absolute;top:2508px;left:0;width:1200px;height:196px;background:var(--footer);color:var(--white);text-align:center}
.footer-links{padding-top:40px;display:flex;justify-content:center;gap:32px;font-size:14px;font-weight:500}
.copyright{margin-top:14px;font-size:12px;color:#bdb8c6}
.social{margin-top:18px;display:flex;justify-content:center;gap:18px}
.social span{width:22px;height:22px;border-radius:50%;background:var(--white)}
</style>
</head>
<body>

<header>
  <div class="topbar">
    <a class="brand" href="#">pelikorax.gr</a>
    <div class="hotline"><small>Αστρολογική<br>πρόβλεψη</small><strong>14877</strong></div>
  </div>
  <nav class="mainnav">
    <a href="#">HOME</a><a href="#">BLOG</a><a href="#">PSYCHIC ASTROLOGERS</a><a href="#">BUY AIRTIME</a><a href="#">PHONE PACKAGES</a>
    <a class="nav-cta" href="#">BUY PACKAGES</a>
  </nav>
</header>

<section class="hero">
  <div class="hero-art" role="img" aria-label="Zodiac wheel with star signs on a night sky"></div>
  <div class="hero-copy">
    <h1>The zodiac signs for today, Friday 18/11</h1>
    <p>Zodiac signs for today 18/11 ARIES Extra obligations appear that require settlement and as soon as possible. You are disappointed by her!</p>
    <a class="btn btn-read" href="#">Read more</a>
  </div>
  <div class="hero-dots"><span></span><span></span><span></span><span></span></div>
</section>

<section class="featured">
  <h2 class="section-title">Featured article</h2>
  <div class="article-grid">
    <article class="article-card"><div class="article-thumb t1" role="img" aria-label="Tarot cards on a table"></div><h3>The zodiac signs<br>for today</h3><div class="article-meta"><i></i>Nov 17, 2022 | <i></i><b>Zodiac Signs</b></div></article>
    <article class="article-card"><div class="article-thumb t2" role="img" aria-label="Crystal jars and candles"></div><h3>The zodiac signs<br>for today</h3><div class="article-meta"><i></i>Nov 17, 2022 | <i></i><b>Zodiac Signs</b></div></article>
    <article class="article-card"><div class="article-thumb t3" role="img" aria-label="Illustrated fortune teller"></div><h3>The zodiac signs<br>for today</h3><div class="article-meta"><i></i>Nov 17, 2022 | <i></i><b>Zodiac Signs</b></div></article>
    <article class="article-card"><div class="article-thumb t4" role="img" aria-label="Candle in a dark room"></div><h3>The zodiac signs<br>for today</h3><div class="article-meta"><i></i>Nov 17, 2022 | <i></i><b>Zodiac Signs</b></div></article>
    <article class="article-card"><div class="article-thumb t5" role="img" aria-label="Glowing heart at sunset"></div><h3>The zodiac signs<br>for today</h3><div class="article-meta"><i></i>Nov 17, 2022 | <i></i><b>Zodiac Signs</b></div></article>
    <article class="article-card"><div class="article-thumb t6" role="img" aria-label="Coffee cup reading"></div><h3>The zodiac signs<br>for today</h3><div class="article-meta"><i></i>Nov 17, 2022 | <i></i><b>Zodiac Signs</b></div></article>
  </div>

  <aside class="sidebar">
    <div class="astro-box">
      <h2>Astrologers</h2>
      <div class="astro-item">
        <div class="astro-head"><div class="astro-photo" role="img" aria-label="Astrologer portrait"></div><div><h4>Elena Marou</h4><p>Powerful psychic.<br>I will help you solve<br>your love and business</p></div></div>
        <a class="btn-call" href="#"><span class="icon"><svg width="18" height="18" viewBox="0 0 24 24"><path fill="#6B429C" d="M6.6 10.8a15 15 0 006.6 6.6l2.2-2.2c.3-.3.7-.4 1-.2 1.1.4 2.3.6 3.6.6.6 0 1 .4 1 1V20c0 .6-.4 1-1 1A17 17 0 013 4c0-.6.4-1 1-1h3.5c.6 0 1 .4 1 1 0 1.3.2 2.5.6 3.6.1.3 0 .7-.2 1z"/></svg></span>Call Now 14877</a>
      </div>
      <div class="astro-item">
        <div class="astro-head"><div class="astro-photo" role="img" aria-label="Astrologer portrait"></div><div><h4>Sofia Vlachou</h4><p>Powerful psychic.<br>I will help you solve<br>your love and business</p></div></div>
        <a class="btn-call" href="#"><span class="icon"><svg width="18" height="18" viewBox="0 0 24 24"><path fill="#6B429C" d="M6.6 10.8a15 15 0 006.6 6.6l2.2-2.2c.3-.3.7-.4 1-.2 1.1.4 2.3.6 3.6.6.6 0 1 .4 1 1V20c0 .6-.4 1-1 1A17 17 0 013 4c0-.6.4-1 1-1h3.5c.6 0 1 .4 1 1 0 1.3.2 2.5.6 3.6.1.3 0 .7-.2 1z"/></svg></span>Call Now 14877</a>
      </div>
      <div class="astro-item">
        <div class="astro-head"><div class="astro-photo" role="img" aria-label="Astrologer portrait"></div><div><h4>Irini Kostaki</h4><p>Powerful psychic.<br>I will help you solve<br>your love and business</p></div></div>
        <a class="btn-call" href="#"><span class="icon"><svg width="18" height="18" viewBox="0 0 24 24"><path fill="#6B429C" d="M6.6 10.8a15 15 0 006.6 6.6l2.2-2.2c.3-.3.7-.4 1-.2 1.1.4 2.3.6 3.6.6.6 0 1 .4 1 1V20c0 .6-.4 1-1 1A17 17 0 013 4c0-.6.4-1 1-1h3.5c.6 0 1 .4 1 1 0 1.3.2 2.5.6 3.6.1.3 0 .7-.2 1z"/></svg></span>Call Now 14877</a>
      </div>
      <a class="btn-more" href="#">Show More</a>
    </div>
    <div class="ad-banner" role="img" aria-label="Offer banner: 30 minutes for 30 euro with stopwatch artwork">
      <span class="ad-time">30'</span>
      <span class="ad-price">30€</span>
    </div>
  </aside>
</section>

<section class="packages">
  <h2>Phone packages offers</h2>
  <svg class="arrow left" width="24" height="30" viewBox="0 0 24 30"><path d="M18 3L6 15l12 12" stroke="#fff" stroke-width="4" fill="none"/></svg>
  <div class="package-row">
    <div class="package-card"><div class="package-top"><h5>PACKAGE 1</h5><div class="price">€30</div><div class="mins">20 Mins</div></div><p>Sed ut perspiciatis unde omnis iste natus error sit voluptatem beatae vitae dicta sunt.</p><a class="btn btn-info" href="#">More Info</a></div>
    <div class="package-card"><div class="package-top"><h5>PACKAGE 2</h5><div class="price">€30</div><div class="mins">20 Mins</div></div><p>Sed ut perspiciatis unde omnis iste natus error sit voluptatem beatae vitae dicta sunt.</p><a class="btn btn-info" href="#">More Info</a></div>
    <div class="package-card"><div class="package-top"><h5>PACKAGE 3</h5><div class="price">€30</div><div class="mins">20 Mins</div></div><p>Sed ut perspiciatis unde omnis iste natus error sit voluptatem beatae vitae dicta sunt.</p><a class="btn btn-info" href="#">More Info</a></div>
    <div class="package-card"><div class="package-top"><h5>PACKAGE 4</h5><div class="price">€30</div><div class="mins">20 Mins</div></div><p>Sed ut perspiciatis unde omnis iste natus error sit voluptatem beatae vitae dicta sunt.</p><a class="btn btn-info" href="#">More Info</a></div>
  </div>
  <svg class="arrow right" width="24" height="30" viewBox="0 0 24 30"><path d="M6 3l12 12L6 27" stroke="#fff" stroke-width="4" fill="none"/></svg>
</section>

<footer class="site-footer">
  <div class="footer-links"><a href="#">CONTACT</a><a href="#">CHARGES</a><a href="#">TERMS OF USE</a><a href="#">BUY AIRTIME</a></div>
  <div class="copyright">Copyright© 2022 Company Name All Rights Reserved</div>
  <div class="social" aria-label="Social links"><span></span><span></span><span></span><span></span></div>
</footer>

</body>
</html>
```